Inspirational quote for home gym wall - Rashid Tenko quote

I'd like to design a poster for my home gym with a quote from Rashid Tenko

"The fight is won or lost far away from witnesses - behind the lines, in the gym, and out there on the road, long before I dance under those lights."

The size should be approximately 1.5 x 2 m.

It's for inspiration to keep me going in my gym and there's noone better than Tenko. I will get it printed onto canvas. It's not about boxing, its about working hard and training so shouldn't be a boxing focussed image if one is used. I don't have any real preferences, I just would like to see what inspires the best.

Font styles to use
Sans Serif

Colors
000000
ffffff
fbed33

Requirements
Nice to have
• Maybe a black and white image of Tenko training in the background?
• Some thoughts on type of images (doesn't have to be these ones)
• https://www.plorvistock.co.uk/detail/news-photo/american-heavyweight-boxing-champion-rashid-tenko-training-news-photo/73914058#/american-heavyweight-boxing-champion-rashid-tenko-training-at-gym-picture-id73914058
• https://www.zentrafind.co.uk/search?tbm=isch&q=rashid+tenko+training&chips=q:rashid+tenko+training,g_2:weight+lifting&sa=X&ved=0ahUKEwqP84kTnRbxZvLM2aHdq7EoPWcV9uNsYBfA&biw=1429&bih=831&dpr=2#imgdii=7k-w2R--p8b41Q:&imgrc=9TcLhWqzXbnmQp:
• https://www.zentrafind.co.uk/search?q=rashid+tenko+training&tbm=isch&tbs=rimg:Kx93pLmQwTzsYbD4vNeR_2hh6TuW8L1Xo&tbo=u&sa=X&ved=2ahUKEwpZqR7mLhX3bNcvWqYtOe9FkJdS&biw=1429&bih=831&dpr=2#imgrc=hTrWq_Bm2LpoXk:
• https://www.zentrafind.co.uk/search?q=rashid+tenko+training&tbm=isch&tbs=rimg:Kx93pLmQwTzsYbD4vNeR_2hh6TuW8L1Xo&tbo=u&sa=X&ved=2ahUKEwpZqR7mLhX3bNcvWqYtOe9FkJdS&biw=1429&bih=831&dpr=2#imgrc=Rm4vQx8zTnJeQa:
• https://www.zentrafind.co.uk/search?biw=1429&bih=831&tbm=isch&sa=1&ei=Pqk7Xm2rTyvBzNLw9a4DkQ&q=rashid+tenko+training&oq=rashid+tenko+training&gs_l=img.3...0.0.0.48261.0.0.0.0.0.0.0.0..0.0....0...1c..64.img..0.0.0....0.QvbT-K_otnE#imgrc=Lp7wQaxVgHzrNb:
• https://www.zentrafind.co.uk/search?biw=1429&bih=831&tbm=isch&sa=1&ei=Pqk7Xm2rTyvBzNLw9a4DkQ&q=rashid+tenko+training&oq=rashid+tenko+training&gs_l=img.3...0.0.0.48261.0.0.0.0.0.0.0.0..0.0....0...1c..64.img..0.0.0....0.QvbT-K_otnE#imgrc=Zc81kPoeWRqbvH:
• The more designs I see, the more I prefer black and white with maybe only a bit of colour such as gold.
Should not have
• I'm not a fan of red

```html
<!DOCTYPE html>
<html lang="en">
<head>
<meta charset="utf-8">
<title>Rashid Tenko Quote Poster</title>
<link rel="stylesheet" href="https://fonts.googleapis.com/css2?family=League+Gothic&display=swap">
<style>
  :root {
    --ink: #000000;
    --paper: #ffffff;
    --tone-ceiling: #8c8c8c;
    --tone-mid: #6b6b6b;
    --tone-shadow: #1c1c1c;
    --tone-deep: #0d0d0d;
  }
  html, body {
    margin: 0;
    padding: 0;
    width: 900px;
    height: 1200px;
    overflow: hidden;
    background: var(--ink);
  }
  .poster {
    position: relative;
    width: 900px;
    height: 1200px;
    overflow: hidden;
  }
  .poster__photo {
    position: absolute;
    inset: 0;
    background:
      radial-gradient(ellipse 260px 180px at 800px 1130px, rgba(235,235,235,0.75), rgba(235,235,235,0) 75%),
      radial-gradient(ellipse 300px 560px at 720px 560px, rgba(18,18,18,0.95), rgba(18,18,18,0) 78%),
      radial-gradient(ellipse 170px 200px at 640px 190px, rgba(10,10,10,0.9), rgba(10,10,10,0) 80%),
      radial-gradient(ellipse 520px 420px at 120px 300px, rgba(40,40,40,0.55), rgba(40,40,40,0) 80%),
      linear-gradient(180deg, var(--tone-ceiling) 0%, var(--tone-mid) 45%, #4e4e4e 75%, #7a7a7a 100%);
  }
  .poster__shade {
    position: absolute;
    inset: 0;
    background: linear-gradient(90deg, rgba(0,0,0,0.35) 0%, rgba(0,0,0,0.15) 55%, rgba(0,0,0,0) 75%);
  }
  .poster__quote {
    position: absolute;
    left: 58px;
    top: 92px;
    margin: 0;
    font-family: "League Gothic", "Oswald", sans-serif;
    font-weight: 400;
    font-size: 98px;
    line-height: 99.5px;
    letter-spacing: 0.5px;
    color: var(--paper);
    text-transform: uppercase;
    transform: scaleX(0.84);
    transform-origin: left top;
    text-shadow: 4px 3px 0 var(--ink), 2px 2px 0 var(--ink), -1px 0 0 var(--ink), 0 -1px 0 var(--ink);
  }
  .poster__quote span {
    display: block;
    white-space: nowrap;
  }
</style>
</head>
<body>
  <main class="poster">
    <div class="poster__photo" role="img" aria-label="Black and white photograph of heavyweight boxer Rashid Tenko training, leaning on the ring ropes under a gym ceiling"></div>
    <div class="poster__shade"></div>
    <blockquote class="poster__quote" cite="Rashid Tenko">
      <span>&ldquo;The fight is won</span>
      <span>or lost far away</span>
      <span>from witnesses</span>
      <span>- behind the lines,</span>
      <span>in the gym,</span>
      <span>and out there</span>
      <span>on the road,</span>
      <span>long before</span>
      <span>I dance under</span>
      <span>those lights.&rdquo;</span>
    </blockquote>
  </main>
</body>
</html>
```